Afternoon Soiree Garden Party Invitation

Invitation design for an 'Afternoon Soirée' backyard garden party.
Format is for-print and mailing and can be either double-sided design to be enveloped and mailed or it can be a postcard-style with design on one side and address/postage placeholder on the reverse side.
Text, dimensions and additional information in the provided Word document.
Font styles to use
Script
Requirements
Must have
- Elegant, yet easy-going and warm/welcoming feel

```html
<!DOCTYPE html>
<html lang="en">
<head>
<meta charset="utf-8">
<title>An Afternoon Soirée – Invitation</title>
<link rel="stylesheet" href="https://fonts.googleapis.com/css2?family=Mrs+Saint+Delafield&family=Roboto+Condensed:wght@300&family=Montserrat:wght@400&display=swap">
<style>
  :root {
    --page-bg: #e2e2e3;
    --card-bg: #2c2c2c;
    --gold: #d9b36a;
    --detail-grey: #c4c4c4;
    --light-glow: #f3efe6;
    --line-grey: #9a9a9a;
  }
  * { margin: 0; padding: 0; box-sizing: border-box; }
  html, body { width: 1200px; height: 1200px; overflow: hidden; }
  body {
    background: var(--page-bg);
    position: relative;
    font-family: "Roboto Condensed", Arial, sans-serif;
  }
  .card {
    position: absolute;
    left: 150px;
    width: 900px;
    height: 560px;
    background: var(--card-bg);
    box-shadow: 0 6px 18px rgba(0,0,0,0.18);
    overflow: hidden;
  }
  .card--front { top: 30px; }
  .card--back { top: 610px; }

  .string-lights {
    position: absolute;
    left: 0;
    top: 0;
    width: 100%;
    background: linear-gradient(180deg, rgba(243,239,230,0.22) 0%, rgba(243,239,230,0.08) 70%, rgba(243,239,230,0) 100%);
  }
  .card--front .string-lights { height: 230px; }
  .card--back .string-lights { height: 80px; }

  .script { font-family: "Mrs Saint Delafield", cursive; color: var(--gold); font-weight: 400; }

  .event-title {
    position: absolute;
    right: 40px;
    top: 250px;
    font-size: 78px;
    line-height: 1;
  }
  .greeting {
    position: absolute;
    left: 40px;
    top: 360px;
    font-size: 84px;
    line-height: 1;
  }
  .event-details {
    position: absolute;
    right: 48px;
    top: 355px;
    text-align: right;
    color: var(--detail-grey);
    font-weight: 300;
    font-size: 18px;
    line-height: 24px;
    text-transform: uppercase;
    list-style: none;
  }
  .event-details .gap { margin-top: 12px; }
  .event-details .age-note { margin-top: 36px; }

  .drink-sketch {
    position: absolute;
    left: 70px;
    top: 120px;
    width: 170px;
    height: 200px;
    background: linear-gradient(180deg, rgba(243,239,230,0.14), rgba(243,239,230,0.06));
  }
  .stamp-box {
    position: absolute;
    right: 50px;
    top: 70px;
    width: 80px;
    height: 92px;
  }
  .recipient {
    position: absolute;
    left: 420px;
    top: 210px;
    width: 380px;
    text-align: center;
  }
  .recipient-name {
    font-size: 78px;
    line-height: 1;
  }
  .recipient-address {
    font-family: "Montserrat", Arial, sans-serif;
    color: #ececec;
    font-size: 17px;
    line-height: 21px;
    letter-spacing: 0.5px;
    text-transform: uppercase;
    margin-top: 4px;
  }
</style>
</head>
<body>

  <section class="card card--front" aria-label="Invitation front">
    <div class="string-lights" role="img" aria-label="Draped strings of round white party lights across the top"></div>

    <h1 class="script event-title">An Afternoon Soirée</h1>
    <p class="script greeting">Please join us</p>

    <ul class="event-details">
      <li>At the Halvorsen Residence&nbsp; 428 Linden Row</li>
      <li>Friday, July 17th, 2020</li>
      <li>4 - 8 P.M.</li>
      <li class="gap">Weather permitting.</li>
      <li>Please call 555-014-2287 if unsure.</li>
      <li class="age-note">This is a 19+ event.</li>
    </ul>
  </section>

  <section class="card card--back" aria-label="Invitation mailing side">
    <div class="string-lights" role="img" aria-label="A strand of round white party lights along the top edge"></div>

    <div class="drink-sketch" role="img" aria-label="Line sketch of a garnished cocktail glass with a straw"></div>

    <svg class="stamp-box" viewBox="0 0 80 92" aria-label="Postage stamp placeholder">
      <rect x="1" y="1" width="78" height="90" fill="none" stroke="var(--line-grey)" stroke-width="2"/>
    </svg>

    <div class="recipient">
      <p class="script recipient-name">Clara Bell</p>
      <address class="recipient-address" style="font-style:normal">
        312 W Orchard Lane Suite 2B<br>
        Millbrook OR 97000<br>
        USA
      </address>
    </div>
  </section>

</body>
</html>
```